All-natural soap packaging design for new company

The box type has been selected, we just need artwork for each of our 10 products. I'd like the same look to each, the idea is just to switch out the name and ingredient label on each. The dimensions are 3.5"x3.75"x1.25". The colors in the uploaded pictures with product titles are not mandatory. I'd like to keep the font on the packaging (Rubik) as it is the same as the website.

Target Market(s)

Health & Beauty, people looking for natural or organic products

Industry/Entity Type

It Company

Colors

Designer to choose colors to be used in the design.

Requirements
Must have
• Design must be clean and relatively simple. Slightly different look for each of the 10 products. Audience is people looking for all-natural products.

```html
<!DOCTYPE html>
<html lang="en">
<head>
<meta charset="utf-8">
<title>Birchwell Soap Co. — Soap Box Fronts</title>
<link href="https://fonts.googleapis.com/css2?family=Rubik:wght@300;400;500&display=swap" rel="stylesheet">
<style>
  :root {
    --canvas: #ffffff;
    --face: #e9e9e9;
    --ink: #45463c;
    --light-text: #f1f1f1;
    --rose: #d96f6a;
    --rose-deep: #c25f5a;
    --rose-lid: #c4645f;
    --rose-text: #d9486a;
    --orange: #e47d1a;
    --orange-deep: #c9660a;
    --orange-lid: #cc6a08;
    --orange-text: #e0601c;
  }
  * { box-sizing: border-box; margin: 0; padding: 0; }
  html, body { width: 1200px; height: 1200px; overflow: hidden; background: var(--canvas); }
  body { font-family: "Rubik", sans-serif; }

  .canvas {
    width: 1200px;
    height: 1200px;
    display: flex;
    justify-content: center;
    align-items: center;
    gap: 60px;
  }

  .box-front {
    width: 440px;
    height: 620px;
    background: var(--face);
    display: flex;
    flex-direction: column;
    box-shadow: 0 18px 30px rgba(0,0,0,0.08);
  }
  .box-front.rose { --accent: var(--rose); --accent-deep: var(--rose-deep); --accent-lid: var(--rose-lid); --accent-text: var(--rose-text); }
  .box-front.orange { --accent: var(--orange); --accent-deep: var(--orange-deep); --accent-lid: var(--orange-lid); --accent-text: var(--orange-text); }

  .lid-band { position: relative; flex: 0 0 48px; background: var(--accent-lid); }
  .lid-notch {
    position: absolute;
    left: 50%;
    top: 48px;
    width: 72px;
    height: 36px;
    margin-left: -36px;
    background: var(--accent-lid);
    border-radius: 0 0 36px 36px;
  }

  .label-area {
    flex: 1 1 auto;
    display: flex;
    flex-direction: column;
    align-items: center;
    justify-content: flex-end;
    padding-bottom: 10px;
  }
  .brand-mark {
    display: flex;
    align-items: center;
    gap: 12px;
    margin-bottom: 110px;
  }
  .brand-square { width: 22px; height: 22px; background: var(--accent-lid); }
  .brand-name {
    font-weight: 500;
    font-size: 27px;
    letter-spacing: 0.02em;
    color: var(--ink);
    text-transform: uppercase;
  }
  .recipe-number {
    font-weight: 400;
    font-size: 26px;
    color: var(--accent-text);
    letter-spacing: 0.01em;
  }

  .product-band {
    flex: 0 0 50px;
    background: var(--ink);
    display: flex;
    align-items: center;
    justify-content: center;
  }
  .product-name {
    font-weight: 300;
    font-size: 31px;
    color: var(--light-text);
    letter-spacing: 0.01em;
  }

  .divider { flex: 0 0 5px; background: var(--face); }

  .pattern-panel {
    flex: 0 0 205px;
    background: radial-gradient(ellipse at 40% 35%, var(--accent) 0%, var(--accent-deep) 100%);
  }
</style>
</head>
<body>
<main class="canvas">
  <section class="box-front rose">
    <div class="lid-band"><div class="lid-notch"></div></div>
    <div class="label-area">
      <div class="brand-mark">
        <span class="brand-square"></span>
        <span class="brand-name">Birchwell Soap Co.</span>
      </div>
      <p class="recipe-number">RECIPE NO.7</p>
    </div>
    <div class="product-band"><h2 class="product-name">PAPAYA+ROSEHIP</h2></div>
    <div class="divider"></div>
    <div class="pattern-panel" role="img" aria-label="Repeating white spiral pattern of assorted sizes on coral pink"></div>
  </section>

  <section class="box-front orange">
    <div class="lid-band"><div class="lid-notch"></div></div>
    <div class="label-area">
      <div class="brand-mark">
        <span class="brand-square"></span>
        <span class="brand-name">Birchwell Soap Co.</span>
      </div>
      <p class="recipe-number">RECIPE NO.8</p>
    </div>
    <div class="product-band"><h2 class="product-name">CARROT+GINGER</h2></div>
    <div class="divider"></div>
    <div class="pattern-panel" role="img" aria-label="Repeating white spiral pattern of assorted sizes on orange"></div>
  </section>
</main>
</body>
</html>
```